Scrap Metal Recycling

We are looking for a simple yet bold business card. We already have the logo, please see attached. Color scheme of blue, black and white or just blue and white.

```html
<!DOCTYPE html>
<html lang="en">
<head>
<meta charset="utf-8">
<title>Harlow Metals Inc. – Business Card</title>
<link rel="stylesheet" href="https://fonts.googleapis.com/css2?family=Montserrat:wght@400;500;600;700&display=swap">
<style>
  :root {
    --stage: #e4e4e3;
    --card-white: #ffffff;
    --charcoal: #373737;
    --charcoal-deep: #2f2f2f;
    --brand-blue: #0a8bb0;
    --ink: #2b2b2b;
    --paper-text: #ffffff;
  }
  * { box-sizing: border-box; margin: 0; padding: 0; }
  html, body {
    width: 1200px; height: 801px; overflow: hidden;
    background: var(--stage);
    font-family: "Montserrat", sans-serif;
  }
  .stage {
    position: relative; width: 1200px; height: 801px;
    display: flex; align-items: center; justify-content: center; gap: 50px;
  }
  .card {
    position: relative; width: 520px; height: 297px; overflow: hidden;
    box-shadow: 0 8px 22px rgba(0,0,0,0.18);
  }
  .card-front { background: var(--card-white); }
  .card-back { background: var(--charcoal); }

  .front-shapes { position: absolute; inset: 0; width: 100%; height: 100%; }
  .band-dark { fill: var(--charcoal); }
  .band-swoosh { fill: var(--brand-blue); }

  .wordmark {
    position: absolute; display: flex; flex-direction: column; align-items: flex-start;
  }
  .wordmark-name {
    font-weight: 700; letter-spacing: 1px; line-height: 1; white-space: nowrap;
  }
  .wordmark-tagline {
    font-weight: 500; color: var(--brand-blue); text-transform: uppercase;
    white-space: nowrap; line-height: 1;
  }
  .card-front .wordmark { left: 64px; top: 30px; }
  .card-front .wordmark-name { font-size: 28px; color: var(--ink); }
  .card-front .wordmark-tagline { font-size: 13px; letter-spacing: 6.4px; margin-top: 8px; }

  .contact-block {
    position: absolute; left: 170px; top: 196px;
    display: flex; align-items: center; gap: 16px; color: var(--paper-text);
  }
  .person { text-align: right; }
  .person-name {
    font-weight: 700; font-size: 16px; letter-spacing: 1px;
    color: var(--brand-blue); text-transform: uppercase; white-space: nowrap;
  }
  .person-role { font-size: 11px; font-weight: 500; margin-top: 3px; }
  .divider { width: 1px; height: 58px; background: var(--paper-text); opacity: 0.85; }
  .contact-list { list-style: none; display: flex; flex-direction: column; gap: 5px; }
  .contact-item { display: flex; align-items: center; gap: 7px; font-size: 11.5px; white-space: nowrap; }
  .contact-icon { width: 13px; height: 13px; flex: none; }

  .back-texture {
    position: absolute; inset: 0;
    background: radial-gradient(ellipse at 50% 50%, #3b3b3b 0%, var(--charcoal-deep) 100%);
  }
  .card-back .wordmark {
    left: 50%; top: 50%; transform: translate(-50%, -50%); align-items: center;
  }
  .card-back .wordmark-name { font-size: 34px; color: var(--paper-text); }
  .card-back .wordmark-tagline { font-size: 15px; letter-spacing: 8.4px; margin-top: 10px; }
</style>
</head>
<body>
<main class="stage">

  <section class="card card-front" aria-label="Business card front">
    <svg class="front-shapes" viewBox="0 0 520 297" preserveAspectRatio="none" aria-hidden="true">
      <path class="band-swoosh" d="M30 297 C 100 180, 290 100, 520 84 L520 94 C 300 110, 120 188, 46 297 Z"/>
      <path class="band-dark" d="M62 297 C 135 198, 310 124, 520 110 L520 297 Z"/>
    </svg>

    <div class="wordmark">
      <span class="wordmark-name">HARLOW METALS INC.</span>
      <span class="wordmark-tagline">Scrap Metal Recycling</span>
    </div>

    <div class="contact-block">
      <div class="person">
        <p class="person-name">Daniel Reeves</p>
        <p class="person-role">Manager</p>
      </div>
      <span class="divider"></span>
      <ul class="contact-list">
        <li class="contact-item">
          <svg class="contact-icon" viewBox="0 0 14 14" aria-hidden="true">
            <circle cx="7" cy="7" r="7" fill="#0a8bb0"/>
            <path d="M4.5 3.8 L6 3.6 L6.5 5.4 L5.6 6 Q6.3 7.7 8 8.4 L8.6 7.5 L10.4 8 L10.2 9.5 Q6.5 10.2 4.5 3.8Z" fill="#fff"/>
          </svg>
          <span>123-456-2100</span>
        </li>
        <li class="contact-item">
          <svg class="contact-icon" viewBox="0 0 14 14" aria-hidden="true">
            <circle cx="7" cy="7" r="7" fill="#0a8bb0"/>
            <rect x="3.5" y="4.5" width="7" height="5" fill="none" stroke="#fff" stroke-width="1"/>
            <path d="M3.5 4.5 L7 7.3 L10.5 4.5" fill="none" stroke="#fff" stroke-width="1"/>
          </svg>
          <span>youremail@mailbox.com</span>
        </li>
        <li class="contact-item">
          <svg class="contact-icon" viewBox="0 0 14 14" aria-hidden="true">
            <circle cx="7" cy="7" r="7" fill="#0a8bb0"/>
            <circle cx="7" cy="7" r="3.6" fill="none" stroke="#fff" stroke-width="0.9"/>
            <ellipse cx="7" cy="7" rx="1.5" ry="3.6" fill="none" stroke="#fff" stroke-width="0.9"/>
            <line x1="3.4" y1="7" x2="10.6" y2="7" stroke="#fff" stroke-width="0.9"/>
          </svg>
          <span>www.yourwebsite.com</span>
        </li>
      </ul>
    </div>
  </section>

  <section class="card card-back" aria-label="Business card back">
    <div class="back-texture" role="img" aria-label="Faint repeating company name pattern across the dark card"></div>
    <div class="wordmark">
      <span class="wordmark-name">HARLOW METALS INC.</span>
      <span class="wordmark-tagline">Scrap Metal Recycling</span>
    </div>
  </section>

</main>
</body>
</html>
```